Premium Olive Oil Bottle Label

Need a double bottle label for our premium olive oil (front and back). Please refer to the brief attached. The label needs to incorporate the elements from the logo designs that we provide in attachment into a single design language. The front panel should capture attention and the back panel provide a story of our unique product.

Target Market(s)

US and Europe

Industry/Entity Type

Food Production

Font styles to use
Other font styles liked:
• Please refer to the Brief

Colors

Designer to choose colors to be used in the design.

Requirements
Must have
• Integrate the elements in the brief into a single premium execution.
Nice to have
• Feel free to use the provided visual elements as a base for your further creative exploration.
Should not have
• Too many colors. Please propose a restricted color palette as the bottle is black matte. The design needs to deliver premium appeal and be distinctive.

```html
<!DOCTYPE html>
<html lang="en">
<head>
<meta charset="utf-8">
<title>Le Haut Vallon – Olive Oil Labels</title>
<link rel="stylesheet" href="https://fonts.googleapis.com/css2?family=Cinzel:wght@400;500&family=EB+Garamond:wght@400&family=Arimo:wght@400;700&display=swap">
<style>
  :root {
    --label-black: #232323;
    --gold: #d9b92e;
    --gold-band: #dfba2c;
    --gold-muted: #a8915a;
    --white: #ffffff;
    --page: #ffffff;
  }
  * { margin: 0; padding: 0; box-sizing: border-box; }
  html, body { width: 1200px; height: 1200px; overflow: hidden; background: var(--page); }
  .canvas { position: relative; width: 1200px; height: 1200px; }

  .front-label {
    position: absolute; left: 162px; top: 255px; width: 461px; height: 695px;
    background: var(--label-black); color: var(--gold); text-align: center;
  }
  .brand-name {
    position: absolute; left: 0; right: 0; top: 330px;
    font-family: "Cinzel", serif; font-weight: 500; color: var(--gold-muted);
    line-height: 1;
  }
  .front-label .brand-name { top: 95px; }
  .brand-name span { display: block; }
  .brand-name .brand-small { font-size: 48px; margin-bottom: 6px; }
  .brand-name .brand-large { font-size: 62px; margin-bottom: 6px; }

  .product-title {
    position: absolute; left: 0; right: 0; top: 592px;
    font-family: "Cinzel", serif; font-weight: 400; font-size: 52px; line-height: 50px;
    color: var(--gold);
  }
  .front-label .product-title { top: 338px; }
  .product-facts {
    position: absolute; left: 0; right: 0; top: 462px;
    font-family: "EB Garamond", serif; font-size: 19.5px; line-height: 26px; color: var(--gold);
  }
  .limited {
    position: absolute; left: 0; right: 0; top: 552px;
    font-family: "Arimo", sans-serif; font-weight: 700; font-size: 31px; color: var(--white);
    letter-spacing: 0.3px;
  }
  .origin-band {
    position: absolute; left: 0; right: 0; top: 603px; height: 29px;
    background: var(--gold-band);
    font-family: "Cinzel", serif; font-size: 15px; line-height: 29px; color: var(--label-black);
  }
  .front-footer {
    position: absolute; top: 655px; font-family: "EB Garamond", serif; font-size: 18.5px; color: var(--gold);
  }
  .front-footer.volume { left: 41px; }
  .front-footer.bottle-no { left: 272px; }

  .back-label {
    position: absolute; left: 652px; top: 106px; width: 331px; height: 990px;
    background: var(--label-black);
  }
  .back-frame {
    position: absolute; left: 21px; top: 20px; width: 296px; height: 953px;
    border: 3px solid var(--gold-band);
  }
  .flourish {
    position: absolute; left: 50%; top: 24px; width: 56px; height: 14px; margin-left: -28px;
    background: var(--gold); border-radius: 7px 7px 3px 3px; opacity: 0.85;
  }
  .story {
    position: absolute; left: 0; right: 0; top: 73px;
    font-family: "Arimo", sans-serif; font-size: 17.5px; line-height: 28px;
    color: var(--gold); text-align: center;
  }
  .story .contact { color: var(--white); }
  .back-mark {
    position: absolute; left: 0; right: 0; top: 890px; text-align: center;
    font-family: "Cinzel", serif; font-weight: 500; color: var(--gold-muted); line-height: 1;
  }
  .back-mark span { display: block; }
  .back-mark .brand-small { font-size: 14px; }
  .back-mark .brand-large { font-size: 17px; }
</style>
</head>
<body>
<div class="canvas">

  <section class="front-label">
    <h1 class="brand-name">
      <span class="brand-small">LE</span>
      <span class="brand-large">HAUT</span>
      <span class="brand-large">VALLON</span>
    </h1>
    <h2 class="product-title">Huile d'Olive<br>Vierge Extra</h2>
    <p class="product-facts">From Provence, Organic, Hand-picked<br>Artisanal, Single cold-press, Unfiltered<br>Late harvest, November 2018</p>
    <p class="limited">LIMITED PRODUCTION</p>
    <div class="origin-band">Made in France</div>
    <p class="front-footer volume">Vol. 500ml</p>
    <p class="front-footer bottle-no">Bottle No:</p>
  </section>

  <section class="back-label">
    <div class="back-frame">
      <div class="flourish" role="img" aria-label="Small gold ornamental flourish"></div>
      <p class="story">
        Nested in the hills of<br>
        Provence, Le Haut Vallon is<br>
        a wild and magical place<br>
        where forest opens up to<br>
        vineyards and olive groves.<br>
        We fell in love with it, and<br>
        you would too! It’s in these<br>
        hills that Aglandau olives<br>
        were grown since Roman<br>
        times, and we were happy to<br>
        bring them back. Our<br>
        production is entirely<br>
        organic, we pick our olives<br>
        by hand and only at the<br>
        point of maturity. We don’t<br>
        harvest our Aglandaus until<br>
        very late in the autumn, and<br>
        use a single mechanical<br>
        cold-press extraction. The<br>
        reward? A very special extra<br>
        virgin oil with its full-on bold<br>
        taste, hints of artichokes and<br>
        fresh-cut grass, and<br>
        remarkably low acidity. Best<br>
        enjoyed before August 2020.<br>
        Do let us know how you<br>
        liked it at<br>
        <span class="contact">info@lehautvallon.com! C+A</span>
      </p>
      <div class="back-mark">
        <span class="brand-small">LE</span>
        <span class="brand-large">HAUT</span>
        <span class="brand-small">VALLON</span>
      </div>
    </div>
  </section>

</div>
</body>
</html>
```